Luminously Grounded Vitality

We want to design a business card that is modern and appealing for an innovative psychedelic telemedicine company that provides at-home ketamine-assisted therapy along with wellness, longevity, and anti-aging medicines. We want to use our deep purple and white plus other colors you can find on our website. We don't have any strict brand guidelines yet so feel free to get creative. We want a very professional, but technology first modern design that will instill trust, peace, calm, but also be attractive to investors in the healthcare and SaaS space.

```html
<!DOCTYPE html>
<html lang="en">
<head>
<meta charset="utf-8">
<title>Luminously Grounded Vitality – Business Card</title>
<link href="https://fonts.googleapis.com/css2?family=Montserrat:wght@400;500;700&display=swap" rel="stylesheet">
<style>
  :root {
    --backdrop: #3b3b3c;
    --brand-purple: #7f69a9;
    --brand-purple-soft: #9484b9;
    --white: #ffffff;
  }
  * { margin: 0; padding: 0; box-sizing: border-box; }
  html, body {
    width: 1200px; height: 1059px; overflow: hidden;
    background: var(--backdrop);
    font-family: "Montserrat", sans-serif;
  }
  .canvas { position: relative; width: 1200px; height: 1059px; }
  .card {
    position: absolute;
    border-radius: 18px;
    overflow: hidden;
    background: var(--brand-purple);
    box-shadow: 0 14px 22px rgba(0,0,0,0.55);
  }
  .card-front { left: 256px; top: 100px; width: 688px; height: 391px; }
  .card-back  { left: 253px; top: 537px; width: 694px; height: 394px; }

  .front-art { position: absolute; inset: 0; }

  .contact-block { position: absolute; left: 36px; top: 78px; color: var(--white); }
  .person-name { font-weight: 700; font-size: 28px; letter-spacing: 1px; line-height: 1; }
  .person-role { font-weight: 400; font-size: 15px; letter-spacing: 0.5px; margin-top: 6px; }
  .address { margin-top: 28px; font-size: 16px; line-height: 20px; letter-spacing: 0.3px; }
  .contact-list { list-style: none; margin-top: 30px; font-size: 16px; letter-spacing: 0.3px; }
  .contact-list li { display: flex; align-items: center; height: 24.7px; }
  .contact-list svg { width: 13px; height: 13px; margin-right: 8px; flex: none; }

  .brand-front {
    position: absolute; left: 343px; width: 360px; top: 0; height: 391px;
    display: flex; flex-direction: column; align-items: center;
  }
  .brand-front .brand-dot {
    width: 96px; height: 96px; border-radius: 50%;
    background: var(--brand-purple); margin-top: 100px;
  }
  .brand-front .brand-name {
    color: var(--brand-purple-soft); font-weight: 500; font-size: 42px;
    margin-top: 40px; letter-spacing: 0.5px;
  }

  .brand-back {
    position: absolute; inset: 0;
    display: flex; flex-direction: column; align-items: center;
  }
  .brand-back .brand-dot {
    width: 120px; height: 120px; border-radius: 50%;
    background: var(--white); margin-top: 92px;
  }
  .brand-back .brand-name {
    color: var(--white); font-weight: 500; font-size: 54px;
    margin-top: 52px; letter-spacing: 0.5px;
  }
</style>
</head>
<body>
<main class="canvas">

  <section class="card card-front" aria-label="Card front">
    <svg class="front-art" viewBox="0 0 688 391" aria-hidden="true">
      <circle cx="548" cy="195.5" r="215" fill="none" stroke="var(--white)" stroke-width="2.5"/>
      <circle cx="543.5" cy="195.5" r="203.5" fill="var(--white)"/>
    </svg>

    <div class="contact-block">
      <h1 class="person-name">DANA WHITFIELD</h1>
      <p class="person-role">MANAGER</p>
      <p class="address">482 Meadowlark Lane 210<br>Your Country, MN 55012</p>
      <ul class="contact-list">
        <li>
          <svg viewBox="0 0 16 16"><path fill="var(--white)" d="M3.6 1.5l2.2 2.6-1.3 1.7c.9 2 2.6 3.7 4.6 4.6l1.7-1.3 2.6 2.2-1.2 2.2C6.7 13.2 2.8 9.3 1.4 3z"/></svg>
          (555)210-4478
        </li>
        <li>
          <svg viewBox="0 0 16 16"><rect x="4" y="1" width="8" height="14" rx="1.5" fill="none" stroke="var(--white)" stroke-width="1.6"/><circle cx="8" cy="12.5" r="0.9" fill="var(--white)"/></svg>
          (555)318-90264
        </li>
        <li>
          <svg viewBox="0 0 16 16"><rect x="1" y="3" width="14" height="10" rx="1" fill="var(--white)"/><path d="M1.5 4l6.5 5 6.5-5" fill="none" stroke="var(--brand-purple)" stroke-width="1.3"/></svg>
          hello@luminouslyvitality.com
        </li>
        <li>
          <svg viewBox="0 0 16 16" fill="none" stroke="var(--white)" stroke-width="1.2"><circle cx="8" cy="8" r="6.5"/><ellipse cx="8" cy="8" rx="3" ry="6.5"/><path d="M1.5 8h13M2.5 4.7h11M2.5 11.3h11"/></svg>
          www.luminouslyvitality.com
        </li>
      </ul>
    </div>

    <div class="brand-front">
      <span class="brand-dot" aria-hidden="true"></span>
      <p class="brand-name">Luminously</p>
    </div>
  </section>

  <section class="card card-back" aria-label="Card back">
    <div class="brand-back">
      <span class="brand-dot" aria-hidden="true"></span>
      <p class="brand-name">Luminously</p>
    </div>
  </section>

</main>
</body>
</html>
```